Clockharbor Homepage Banner 1060 W x 100 H

Please see the attached 'word' document (Also copied below)
Feel free to use any images or logos from our website.
www.clockharbor.com.au

Background:
We are an Australian based official watch distributor/online retailer of international watch brands.

We require a new banner ad (1060 W x 100 H) to replace the existing one on our homepage www.clockharbor.com.au & wish to convey the following information:
*(Please feel free to alter wording, include or exclude points below & generally take creative license (with commercial reality in mind). We sell some luxury watches, so it must look professional & maintain a luxury look & feel.)

Clockharbor Direct:
Revolutionising the retail watch market !

- Buy direct from the official distributor & get world competitive
online prices (with full international warranty, & all original
papers, box & invoice)

- Eliminate all risk of fakes & non-existent factory warranty from
'grey' market sellers

- Free worldwide delivery over A$300

- Order online & 'try-on' in the comfort of your own home.
If you're not 100% happy, just post it back for a full refund or
exchange within 30 days

- Prefer to see & try on before purchase? Visit one of our retail
partner stores.

*** Feel free to copy any images from our website
www.clockharbor.com.au
Updates

Target Market(s)

Luxury watches

Industry/Entity Type

Retail

Font styles to use
Sans Serif

Requirements
Must have
• Visual imagery, text
Nice to have
• Feel free to use your creativity...
Should not have
• Cheap looking or tacky images. We sell some luxury watches, so we need to keep a professional & luxury image.

```html
<!DOCTYPE html>
<html lang="en">
<head>
<meta charset="utf-8">
<title>Clockharbor Homepage Banner</title>
<link rel="stylesheet" href="https://fonts.googleapis.com/css2?family=Bebas+Neue&family=Raleway:wght@600&family=Comfortaa:wght@500&display=swap">
<style>
  :root {
    --stage: #8c8c8c;
    --paper: #ffffff;
    --navy: #0b2767;
    --gold-light: #d2b47a;
    --gold-dark: #ad8c52;
    --watch-dark: #1c1c1e;
    --watch-steel: #b9b9bb;
    --brand-ink: #1b2f6e;
  }
  * { box-sizing: border-box; margin: 0; padding: 0; }
  html, body { width: 1200px; height: 1200px; overflow: hidden; }
  body { background: var(--stage); position: relative; }

  .banner {
    position: absolute;
    left: 23px; top: 546px;
    width: 1155px; height: 108px;
    background: var(--paper);
    overflow: hidden;
  }
  .product-photo {
    position: absolute;
    left: 0; top: 0;
    width: 310px; height: 108px;
    background: radial-gradient(ellipse 48% 130% at 50% 100%, var(--watch-dark) 0 82%, var(--watch-steel) 83% 92%, var(--paper) 93%);
  }
  .brand {
    position: absolute;
    left: 332px; top: 32px;
    display: flex; align-items: center; gap: 10px;
  }
  .brand-dot {
    width: 42px; height: 42px; border-radius: 50%;
    background: var(--navy);
  }
  .brand-name {
    font-family: "Comfortaa", sans-serif;
    font-weight: 500;
    font-size: 30px;
    color: var(--brand-ink);
    letter-spacing: 0.3px;
  }
  .offer-panel {
    position: absolute; left: 0; top: 0;
    width: 1155px; height: 108px;
  }
  .offer {
    position: absolute;
    left: 650px; top: 14px;
    width: 310px;
    text-align: center;
    color: var(--paper);
    font-family: "Bebas Neue", sans-serif;
    line-height: 1;
  }
  .offer-lead { font-size: 27px; letter-spacing: 0.6px; }
  .offer-amount { font-size: 64px; letter-spacing: 1.5px; margin-top: 1px; }
  .cta {
    position: absolute;
    left: 950px; top: 32px;
    width: 184px; height: 42px;
    border-radius: 6px;
    background: linear-gradient(var(--gold-light), var(--gold-dark));
    box-shadow: 0 3px 0 #8f7240;
    color: var(--paper);
    font-family: "Raleway", sans-serif;
    font-weight: 600;
    font-size: 25px;
    line-height: 42px;
    text-align: center;
    text-decoration: none;
  }
</style>
</head>
<body>
  <section class="banner">
    <div class="product-photo" role="img" aria-label="Close-up of a black-dial pilot watch in a steel case"></div>

    <div class="brand">
      <span class="brand-dot"></span>
      <span class="brand-name">Clockharbor</span>
    </div>

    <svg class="offer-panel" viewBox="0 0 1155 108" aria-hidden="true">
      <polygon points="647,0 1155,0 1155,108 590,108" fill="var(--navy)"/>
    </svg>

    <div class="offer">
      <p class="offer-lead">Free Worldwide Delivery</p>
      <p class="offer-amount">Over A$300</p>
    </div>

    <a class="cta" href="#">SHOP NOW!</a>
  </section>
</body>
</html>
```